Corporate Business card, Letter head, & Envelope
CorvaneLG
Professional
Nadia Perrow
CEO
5827 Fenwillow Dr, Suite 408
Larkhaven, Texas 75099
nadiap@corvaneloftsgroup.example
www.corvaneloftsgroup.example
We are a corporate travel management and not a leisure company, so we need to stay professional

```html
<!DOCTYPE html>
<html lang="en">
<head>
<meta charset="utf-8">
<title>CorvaneLG Business Card</title>
<link href="https://fonts.googleapis.com/css2?family=PT+Sans:wght@400;700&display=swap" rel="stylesheet">
<style>
  :root {
    --page: #eceef1;
    --navy: #1f3a8f;
    --blue-deep: #1b2a86;
    --blue-mid: #3558c4;
    --blue-light: #5f86e0;
    --orange: #f08a1c;
    --ink: #3c3f46;
    --white: #ffffff;
  }
  * { box-sizing: border-box; margin: 0; padding: 0; }
  html, body { width: 1200px; height: 1009px; overflow: hidden; }
  body {
    background: var(--page);
    font-family: "PT Sans", Arial, sans-serif;
    position: relative;
  }
  .card {
    position: absolute;
    width: 560px;
    height: 320px;
    border-radius: 18px;
    overflow: hidden;
    box-shadow: 0 6px 18px rgba(0,0,0,.12);
  }
  /* back side */
  .card-back {
    left: 560px; top: 120px;
    background: radial-gradient(circle at 60% 45%, var(--blue-light) 0%, var(--blue-mid) 45%, var(--blue-deep) 100%);
    color: var(--white);
  }
  .card-back .brand { position: absolute; left: 150px; top: 26px; }
  .card-back .brand-name { font-size: 24px; font-weight: 700; letter-spacing: 1px; text-transform: uppercase; }
  .card-back .brand-tag { font-size: 10px; letter-spacing: 2px; text-transform: uppercase; margin-top: 2px; }
  .card-back .world-art {
    position: absolute; left: 150px; top: 90px;
    width: 360px; height: 200px; border-radius: 40% 50% 45% 40%;
    background: radial-gradient(ellipse at center, rgba(255,255,255,.55) 0%, rgba(255,255,255,.2) 55%, rgba(255,255,255,0) 75%);
  }
  /* front side */
  .card-front {
    left: 80px; top: 500px;
    background: var(--white);
    color: var(--ink);
  }
  .logo {
    position: absolute; left: 34px; top: 78px;
    display: flex; align-items: center; gap: 10px;
  }
  .logo-mark { width: 30px; height: 30px; background: var(--navy); border-radius: 4px; }
  .logo-name { font-size: 28px; font-weight: 700; color: var(--navy); }
  .logo-tag {
    position: absolute; left: 34px; top: 120px;
    font-size: 10px; letter-spacing: 2px; color: var(--orange); text-transform: uppercase;
  }
  .contact { position: absolute; left: 300px; top: 56px; }
  .person-name { font-size: 22px; font-weight: 700; color: var(--navy); }
  .person-title { font-size: 14px; color: var(--orange); margin-bottom: 14px; }
  .address { font-size: 12.5px; line-height: 1.4; margin-bottom: 8px; }
  .lines { list-style: none; font-size: 12.5px; line-height: 1.6; }
  .lines li { display: flex; align-items: center; gap: 6px; white-space: nowrap; }
  .lines svg { width: 11px; height: 11px; fill: var(--orange); flex: none; }
  .toll { color: var(--navy); }
  .rule { position: absolute; left: 0; right: 0; bottom: 42px; height: 4px; background: var(--orange); }
  .web-band {
    position: absolute; left: 0; right: 0; bottom: 0; height: 42px;
    background: linear-gradient(90deg, var(--blue-deep), var(--blue-mid));
    color: var(--white); font-size: 14px; letter-spacing: 3px;
    display: flex; align-items: center; padding-left: 34px;
  }
</style>
</head>
<body>
  <section class="card card-back">
    <div class="brand">
      <div class="brand-name">CorvaneLG</div>
      <div class="brand-tag">Travel Management Company</div>
    </div>
    <div class="world-art" role="img" aria-label="World map illustration with orbit swoosh and open door"></div>
  </section>

  <section class="card card-front">
    <div class="logo">
      <span class="logo-mark"></span>
      <span class="logo-name">CorvaneLG</span>
    </div>
    <div class="logo-tag">Travel Management Company</div>

    <div class="contact">
      <div class="person-name">Nadia Perrow</div>
      <div class="person-title">CEO</div>
      <div class="address">5827 Fenwillow Dr, Suite 408<br>Larkhaven, Texas 75099</div>
      <ul class="lines">
        <li><svg viewBox="0 0 12 12"><path d="M2 1h3l1 3-2 1a7 7 0 0 0 3 3l1-2 3 1v3a1 1 0 0 1-1 1A10 10 0 0 1 1 2a1 1 0 0 1 1-1z"/></svg>800-555-0142 <span class="toll">(Toll Free)</span></li>
        <li><svg viewBox="0 0 12 12"><path d="M2 1h3l1 3-2 1a7 7 0 0 0 3 3l1-2 3 1v3a1 1 0 0 1-1 1A10 10 0 0 1 1 2a1 1 0 0 1 1-1z"/></svg>972-555-0187</li>
        <li><svg viewBox="0 0 12 12"><rect x="1" y="4" width="10" height="6" rx="1"/><rect x="3" y="1" width="6" height="3"/></svg>972-555-0163</li>
        <li><svg viewBox="0 0 12 12"><path d="M1 2h10v8H1z M1 2l5 4 5-4" stroke="#fff" stroke-width=".8"/></svg>nadiap@corvaneloftsgroup.example</li>
      </ul>
    </div>

    <div class="rule"></div>
    <div class="web-band">www.corvaneloftsgroup.example</div>
  </section>
</body>
</html>
```